Post Card Invitation to Wedding Rehearsal Dinner and After Party

This post card should serve as invitations for two events in the wedding weekend for two San Francisco grooms, Derek and Leon.
Each side of the card should have distinct looks and information but tied together with “Before” on the front and “After” on the back.
POST CARD FRONT
Required text:
BEFORE
Derek and Leon’s Wedding: Rehearsal Dinner
Friday, May 22, 2015
5:30 PM
Larkfield Kitchen Yard
615 Fenwick Street @ Marlow
San Francisco, CA
Please also convey the following information without necessarily quoting directly: This rehearsal dinner will be held in a private enclosed space in the food truck park. We we will serve beer and wine in our space and provide tickets to purchase food from any of the trucks in the park. Dress is casual.
Look and feel of the card should have a modern, “hipster” feel to it. If you search Google images for “Hipster design” or “hipster infographic” you should get a sense of the overall design and colors. The website for the venue is http://larkfieldkitchenyard.com/ for reference but please DO NOT use any images or logos from the site.
----------------------
POST CARD REVERSE
Required Text:
AFTER
Derek and Leon’s Wedding: After Party
Saturday, May 23, 2015
7:30 PM
Harbor Crest Sailing Club
47 Pelling Road
San Francisco, CA
Please also convey the following information without necessarily quoting directly: Black-tie optional. Dancing, snacks and dessert and cocktails with panoramic views of the San Francisco Bay and Golden Gate Bridge.
This should have a much different look and feel from the front of the card. It should convey an elegant black-tie affair. If you search Google images for “black tie after party invitation” you should get some examples of an overall feel that I am aiming for. The website for the venue is www.hcsailclub.com but DO NOT use any of the images or logos from the site.
Industry/Entity Type
Wedding
Look and feel
Each slider illustrates characteristics of the customer's brand and the style your logo design should communicate.

```html
<!DOCTYPE html>
<html lang="en">
<head>
<meta charset="utf-8">
<title>Derek &amp; Leon's Wedding: Rehearsal Dinner</title>
<link rel="stylesheet" href="https://fonts.googleapis.com/css2?family=Great+Vibes&family=Caveat+Brush&family=Arimo:wght@400;700&family=Cabin+Condensed:wght@400&display=swap">
<style>
  :root {
    --night: #07060b;
    --teal-haze: #2c5a66;
    --violet-haze: #7a3fb0;
    --magenta-haze: #b13a90;
    --frame: #6e6c3c;
    --title-lime: #d3e21e;
    --detail-yellow: #e4d935;
    --white: #ffffff;
    --plate-light: #f2f2f2;
    --plate-shade: #bfbfbf;
  }
  * { margin: 0; padding: 0; box-sizing: border-box; }
  html, body { width: 1200px; height: 800px; overflow: hidden; background: var(--night); }
  .invitation {
    position: relative;
    width: 1200px;
    height: 800px;
    overflow: hidden;
    background: var(--night);
  }
  .nebula-backdrop {
    position: absolute;
    inset: 0;
    background:
      radial-gradient(ellipse 260px 220px at 560px 300px, rgba(235,215,255,0.55), transparent 70%),
      radial-gradient(ellipse 330px 300px at 300px 360px, rgba(60,120,135,0.75), transparent 70%),
      radial-gradient(ellipse 380px 330px at 640px 420px, rgba(122,63,176,0.85), transparent 70%),
      radial-gradient(ellipse 360px 320px at 900px 420px, rgba(177,58,144,0.8), transparent 70%),
      radial-gradient(ellipse 300px 240px at 700px 120px, rgba(110,50,160,0.6), transparent 70%),
      var(--night);
  }
  .card-frame {
    position: absolute;
    left: 38px; top: 38px;
    width: 1128px; height: 726px;
    border: 4px solid var(--frame);
    border-radius: 20px;
  }
  .event-label {
    position: absolute;
    top: 100px; left: 0; width: 100%;
    text-align: center;
    font-family: "Great Vibes", cursive;
    font-size: 76px;
    color: var(--white);
    line-height: 1;
  }
  .event-title {
    position: absolute;
    top: 212px; left: 0; width: 100%;
    text-align: center;
    font-family: "Caveat Brush", cursive;
    font-size: 58px;
    color: var(--title-lime);
    line-height: 1;
    letter-spacing: 1px;
  }
  .event-date {
    position: absolute;
    top: 366px; left: 0; width: 100%;
    text-align: center;
    font-family: "Arimo", sans-serif;
    font-weight: 700;
    font-size: 36px;
    color: var(--white);
  }
  .event-venue {
    position: absolute;
    top: 444px; left: 0; width: 100%;
    text-align: center;
    font-family: "Arimo", sans-serif;
    font-size: 18px;
    line-height: 27px;
    color: var(--white);
  }
  .event-notes {
    position: absolute;
    top: 562px; left: 240px; width: 720px;
    text-align: center;
    font-family: "Cabin Condensed", sans-serif;
    font-size: 22px;
    line-height: 31.5px;
    color: var(--detail-yellow);
  }
  .place-setting {
    position: absolute;
    top: 612px;
    width: 230px; height: 146px;
    border-radius: 115px 115px 0 0;
    background: radial-gradient(ellipse at 50% 70%, var(--plate-light) 45%, var(--plate-shade) 100%);
  }
  .place-setting--left { left: 42px; }
  .place-setting--right { left: 928px; }
</style>
</head>
<body>
<main class="invitation">
  <div class="nebula-backdrop" role="img" aria-label="Starry night sky with teal, violet and magenta nebula clouds and crossing light beams"></div>
  <div class="card-frame"></div>

  <p class="event-label">Before</p>
  <h1 class="event-title">Derek &amp; Leon's Wedding: Rehearsal Dinner</h1>

  <p class="event-date">Friday, May 22, 2015</p>
  <p class="event-venue">
    5:30 PM<br>
    Larkfield Kitchen Yard<br>
    615 Fenwick Street @ Marlow,&nbsp; San Francisco, CA
  </p>

  <p class="event-notes">
    This rehearsal dinner will be held in a private<br>
    enclosed space in the food truck park. We we will serve beer and<br>
    wine in our space and provide tickets to purchase food from any<br>
    of the trucks in the park. Dress is casual.
  </p>

  <div class="place-setting place-setting--left" role="img" aria-label="White dinner plate with fork, knife and spoon"></div>
  <div class="place-setting place-setting--right" role="img" aria-label="White dinner plate with spoon, knife and fork"></div>
</main>
</body>
</html>
```